App Redesign for PathMentor

We're looking for a skilled UI/UX designer to modernize the PathMentor mobile app, enhancing user engagement while preserving our current brand identity.

Key Objectives:
Refresh the app using modern design trends
Maintain a clean, calm, and playful aesthetic aligned with our brand
Boost engagement through improved flow, visuals, and interactivity

Design Requirements:
Retain recognizability from our app and website (see Brand ID Guide) (and website pathmentorhub.example)
Reflect a tone that is supportive, fun/ playful, and professional

Design 5–8 key screens, including:
Home/Dashboard
Daily Intentions Interface
Gamification Overview (Streaks, Rewards)
Social Features (Direct Realtime Feedback, Messaging, Challenges)
Progress Tracking

New Feature Concepts to Include:
Daily Intentions with voice/text input and visual encouragement
Gamification elements like streaks, badges, and animations
Social Connections including messaging, reactions, and feedback tools
Optional: Subtle design cues for future AI-driven interactions

Audience: Adults aged 25–55 interested in personal development and coaching. Tech-comfortable but not tech-savvy.

Visual Inspiration: Wordivo (gamification), Calmnest (intentions), Runqo (social support)

Target Market(s)

Corporate Leaders and Entrepreneurs

Industry/Entity Type

Leadership Training & Consultancies

Font styles to use
Sans Serif
Other font styles liked:
• Avenir, Arial

Colors
FFF300
FFF600
FEFA6F
FFFEC7
FFFEE8

Requirements
Nice to have
• Wordivo, Calmnest,

```html
<!DOCTYPE html>
<html lang="en">
<head>
<meta charset="utf-8">
<title>PathMentor – Home Dashboard</title>
<link rel="stylesheet" href="https://fonts.googleapis.com/css2?family=Outfit:wght@400;500;600;700;800&display=swap">
<style>
  :root {
    --brand-yellow: #ffd800;
    --ink: #000000;
    --paper: #ffffff;
    --stone: #b5aca6;
    --nav-bg: #f3f3f3;
    --nav-muted: #8a8a8a;
    --nav-active: #222222;
    --frame-line: #3a3a3a;
    --ring-track: #6b6b6b;
    --backdrop-center: #ffffff;
    --backdrop-edge: #dcdcdc;
  }
  * { margin: 0; padding: 0; box-sizing: border-box; }
  html, body { width: 1200px; height: 891px; overflow: hidden; }
  body {
    font-family: "Outfit", sans-serif;
    background: radial-gradient(ellipse at center, var(--backdrop-center) 35%, var(--backdrop-edge) 100%);
  }
  .stage {
    position: absolute; left: 0; top: 0;
    width: 1401px; height: 1041px;
    transform: scale(0.8565); transform-origin: 0 0;
  }
  .screen {
    position: absolute; left: 469px; top: 87px;
    width: 464px; height: 867px;
    background: var(--paper);
    border: 1px solid var(--frame-line);
    overflow: hidden;
  }
  .abs { position: absolute; }

  /* brand */
  .brand { left: 34px; top: 44px; display: flex; align-items: center; gap: 14px; }
  .brand-dot { width: 44px; height: 44px; border-radius: 50%; background: var(--brand-yellow); }
  .brand-name { font-size: 28px; font-weight: 600; color: var(--brand-yellow); letter-spacing: -0.2px; }

  /* stat cards */
  .stat-card { top: 119px; width: 186px; height: 132px; padding: 0 0 0 24px; }
  .stat-card--weekly { left: 36px; background: var(--ink); }
  .stat-card--monthly { left: 243px; background: var(--brand-yellow); padding-left: 19px; }
  .stat-icon { position: absolute; top: 0; left: 24px; }
  .stat-card--monthly .stat-icon { left: 20px; }
  .stat-value {
    position: absolute; top: 40px; font-size: 72px; font-weight: 800;
    line-height: 1; letter-spacing: -2px;
  }
  .stat-card--weekly .stat-value { color: var(--paper); }
  .stat-card--monthly .stat-value { color: var(--paper); }
  .stat-label { position: absolute; top: 100px; font-size: 20px; font-weight: 500; white-space: nowrap; }
  .stat-card--weekly .stat-label { color: var(--brand-yellow); }
  .stat-card--monthly .stat-label { color: var(--ink); }

  .section-title { left: 39px; font-size: 24px; font-weight: 500; color: var(--ink); }
  .section-title--progress { top: 283px; }
  .section-title--growth { top: 547px; }

  .progress-chart { left: 30px; top: 310px; }

  .summary-bar { left: 39px; top: 474px; width: 275px; height: 65px; background: var(--stone); }
  .summary-badge {
    left: 338px; top: 473px; width: 92px; height: 65px; background: var(--brand-yellow);
    color: var(--paper); text-align: center;
  }
  .summary-badge .value { display: block; font-size: 26px; font-weight: 700; margin-top: 9px; line-height: 1; }
  .summary-badge .caption { display: block; font-size: 13px; margin-top: 5px; }

  .growth-panel { left: 39px; top: 578px; width: 391px; height: 214px; background: var(--ink); }
  .growth-question {
    position: absolute; left: 53px; top: 21px; width: 300px;
    font-size: 16px; font-weight: 500; line-height: 19px; color: var(--brand-yellow);
  }
  .growth-question strong { color: var(--paper); font-weight: 600; }
  .growth-rings { position: absolute; left: 0; top: 0; }
  .ring-value { font-family: "Outfit", sans-serif; font-size: 29px; font-weight: 700; fill: var(--brand-yellow); }

  .tab-bar {
    left: 0; top: 791px; width: 464px; height: 76px; background: var(--nav-bg);
    display: flex;
  }
  .tab { width: 100px; text-align: center; color: var(--nav-muted); font-size: 9px; font-weight: 500; }
  .tab:first-child { margin-left: 30px; }
  .tab svg { display: block; margin: 21px auto 3px; }
  .tab--active { color: var(--nav-active); font-weight: 600; }
</style>
</head>
<body>
<div class="stage">
  <main class="screen">
    <header class="abs brand">
      <span class="brand-dot"></span>
      <span class="brand-name">PathMentor</span>
    </header>

    <section class="abs stat-card stat-card--weekly">
      <svg class="stat-icon" width="30" height="32" viewBox="0 0 30 32">
        <rect x="3" y="5" width="24" height="25" rx="2" fill="none" stroke="#fff" stroke-width="3"/>
        <rect x="3" y="5" width="24" height="7" fill="#fff"/>
        <rect x="9" y="16" width="12" height="3" fill="#fff"/>
        <rect x="8" y="0" width="3" height="6" fill="#fff"/><rect x="19" y="0" width="3" height="6" fill="#fff"/>
      </svg>
      <span class="stat-value">271</span>
      <span class="stat-label">Weekly Reports</span>
    </section>

    <section class="abs stat-card stat-card--monthly">
      <svg class="stat-icon" width="30" height="32" viewBox="0 0 30 32">
        <rect x="3" y="5" width="24" height="25" rx="2" fill="none" stroke="#fff" stroke-width="3"/>
        <rect x="3" y="5" width="24" height="7" fill="#fff"/>
        <g fill="#fff"><rect x="8" y="15" width="4" height="4"/><rect x="13" y="15" width="4" height="4"/><rect x="18" y="15" width="4" height="4"/>
        <rect x="8" y="21" width="4" height="4"/><rect x="13" y="21" width="4" height="4"/><rect x="18" y="21" width="4" height="4"/></g>
        <rect x="8" y="0" width="3" height="6" fill="#fff"/><rect x="19" y="0" width="3" height="6" fill="#fff"/>
      </svg>
      <span class="stat-value">75</span>
      <span class="stat-label">Monthly Reports</span>
    </section>

    <h2 class="abs section-title section-title--progress">Your Overall Progress</h2>

    <svg class="abs progress-chart" width="400" height="150" viewBox="0 0 400 150" role="img" aria-label="Progress bar chart">
      <line x1="9" y1="3" x2="9" y2="123" stroke="#999" stroke-width="1"/>
      <line x1="9" y1="122.5" x2="381" y2="122.5" stroke="#999" stroke-width="1"/>
      <g fill="var(--brand-yellow)">
        <rect x="10" y="18" width="356" height="17"/>
        <rect x="10" y="44" width="241" height="17"/>
        <rect x="10" y="70" width="292" height="18"/>
        <rect x="10" y="97" width="327" height="17"/>
      </g>
      <g font-family="Outfit, sans-serif" font-size="12" fill="#000" text-anchor="middle">
        <text x="11" y="140">50</text><text x="102" y="140">100</text><text x="194" y="140">150</text>
        <text x="286" y="140">200</text><text x="378" y="140">250</text>
      </g>
    </svg>

    <div class="abs summary-bar"></div>
    <div class="abs summary-badge"><span class="value">75%</span><span class="caption">Text</span></div>

    <h2 class="abs section-title section-title--growth">Your Overall Growth</h2>

    <section class="abs growth-panel">
      <p class="growth-question"><strong>BODY:</strong> Did I take a cold shower or swim in the river today?</p>
      <svg class="growth-rings" width="391" height="214" viewBox="0 0 391 214">
        <g fill="none" stroke-width="3">
          <circle cx="81" cy="130" r="44" stroke="var(--ring-track)" stroke-width="1.5"/>
          <path d="M81 86 A44 44 0 0 1 81 174" stroke="#fff"/>
          <circle cx="195" cy="130" r="44" stroke="var(--ring-track)" stroke-width="1.5"/>
          <path d="M195 86 A44 44 0 1 1 151 130" stroke="#fff"/>
          <circle cx="307" cy="130" r="44" stroke="#fff"/>
        </g>
        <text class="ring-value" x="80" y="140" text-anchor="middle">50%</text>
        <text class="ring-value" x="194" y="140" text-anchor="middle">75%</text>
        <text class="ring-value" x="307" y="140" text-anchor="middle">99%</text>
      </svg>
    </section>

    <nav class="abs tab-bar">
      <div class="tab tab--active">
        <svg width="20" height="18" viewBox="0 0 20 18"><path d="M2 9 L10 2 L18 9 M4.5 7.5 V16 H8.5 V11 H11.5 V16 H15.5 V7.5" fill="none" stroke="currentColor" stroke-width="1.8" stroke-linejoin="round"/></svg>
        Home
      </div>
      <div class="tab">
        <svg width="20" height="18" viewBox="0 0 20 18"><path d="M2 2 V16 H18 M6 13 V8 M9 13 V5 M12 13 V9 M15 13 V6" fill="none" stroke="currentColor" stroke-width="1.6"/></svg>
        Reports
      </div>
      <div class="tab">
        <svg width="20" height="18" viewBox="0 0 20 18"><rect x="2.5" y="3" width="15" height="14" rx="1" fill="none" stroke="currentColor" stroke-width="1.6"/><rect x="2.5" y="3" width="15" height="4" fill="currentColor"/><rect x="8" y="10" width="4" height="4" fill="currentColor"/><path d="M6 0 V4 M14 0 V4" stroke="currentColor" stroke-width="1.6"/></svg>
        Questions
      </div>
      <div class="tab">
        <svg width="20" height="18" viewBox="0 0 20 18"><path d="M2 3 H18 M2 9 H18 M2 15 H18" stroke="currentColor" stroke-width="1.8"/></svg>
        More
      </div>
    </nav>
  </main>
</div>
</body>
</html>
```